https://copperwillowbrambleyard.org/

We would like the website to represent 19th century African American civil war soldier's letters. We would like the site colors to be nice and clean . Along with the layout, including a great landing page , blogs and introduction.

```html
<!DOCTYPE html>
<html lang="en">
<head>
<meta charset="utf-8">
<title>Copper Willow Brambleyard</title>
<link rel="stylesheet" href="https://fonts.googleapis.com/css2?family=Poppins:wght@300;400;500;600&family=Montserrat:wght@400;500&display=swap">
<style>
:root{
  --navy:#1d3059;
  --navy-deep:#1a2b52;
  --orange:#e59e5f;
  --orange-text:#e8a063;
  --white:#ffffff;
  --ink:#2a2a2a;
  --muted:#555a66;
  --footer:#1f1f1f;
  --line:#c9ccd4;
  --quote-gray:#e6e6e6;
}
*{margin:0;padding:0;box-sizing:border-box}
html,body{width:1200px;height:3329px;overflow:hidden}
body{font-family:"Montserrat",sans-serif;background:var(--white);position:relative;color:var(--ink)}
.abs{position:absolute}
.navy-zone{position:absolute;left:0;top:0;width:1200px;height:2227px;background:var(--navy);overflow:hidden}

/* header */
.brand{left:75px;top:22px;display:flex;align-items:center;gap:12px;color:var(--white);font-family:"Poppins",sans-serif;font-weight:600;font-size:19px;line-height:1}
.brand-dot{width:26px;height:26px;border-radius:50%;background:var(--orange)}
.nav{right:118px;top:29px;display:flex;gap:26px;font-size:13px;color:var(--white);font-family:"Poppins",sans-serif;font-weight:300}
.nav a{color:inherit;text-decoration:none;position:relative}
.nav a.active::after{content:"";position:absolute;left:0;right:0;bottom:-12px;height:2px;background:var(--orange)}
.search{right:75px;top:28px}

/* hero */
.hero-card{left:109px;top:145px;width:1014px;height:505px;background:var(--white)}
.hero-photo{left:75px;top:113px;width:523px;height:484px;background:linear-gradient(135deg,#2c2016 0%,#a98257 35%,#d7b78c 60%,#6a4a2e 100%)}
.hero-text{left:660px;top:200px;width:400px}
.eyebrow{color:var(--orange-text);font-size:14px;font-family:"Poppins",sans-serif;font-weight:300}
.hero-title{margin-top:12px;font-family:"Poppins",sans-serif;font-weight:300;font-size:39px;line-height:45px;color:var(--ink)}
.hero-para{margin-top:36px;font-size:12px;line-height:19px;color:var(--muted)}
.hero-para+.hero-para{margin-top:18px}
.meta{left:660px;top:562px;display:flex;align-items:center;font-size:14px;color:var(--orange-text);font-family:"Poppins",sans-serif;font-weight:300}
.meta span{display:flex;align-items:center;gap:9px}
.meta .sep{width:1px;height:40px;background:#ddd;margin:0 22px}

/* carousel */
.card{top:733px;width:285px}
.card-photo{width:285px;height:285px}
.card-title{margin-top:20px;color:var(--white);font-family:"Poppins",sans-serif;font-weight:300;font-size:15px;line-height:17px}
.read{margin-top:24px;display:flex;align-items:center;gap:12px;color:var(--orange-text);font-family:"Poppins",sans-serif;font-weight:300;font-size:14px}
.arrow-btn{width:44px;height:44px;border-radius:50%;background:var(--white);display:flex;align-items:center;justify-content:center;top:854px}

/* newsletter */
.deco-right{left:953px;top:1168px;width:384px;height:384px;border-radius:50%;background:linear-gradient(200deg,#1d3059 10%,#7a5d57 70%,#8d6d5f 100%)}
.newsletter{left:75px;top:1248px;width:1048px;height:232px;background:var(--orange)}
.follow{left:103px;top:92px;font-family:"Poppins",sans-serif;font-weight:300;font-size:38px;color:var(--ink)}
.news-note{left:473px;top:72px;font-size:13px;color:var(--ink)}
.email-field{left:473px;top:114px;width:437px;height:45px;border:1px solid #444}
.email-field span{position:absolute;left:18px;top:14px;font-size:12px;letter-spacing:4px;color:var(--ink)}
.send-btn{left:868px;top:120px;width:78px;height:32px;background:var(--navy);display:flex;align-items:center;justify-content:center}

/* about */
.deco-left{left:12px;top:1677px;width:450px;height:450px;border-radius:50%;background:linear-gradient(160deg,#1d3059 0%,#6a5455 60%,#8b6a5d 100%)}
.portrait{left:65px;top:1611px;width:442px;height:442px;border-radius:50%;background:radial-gradient(circle at 50% 45%,#bdbdbd 0%,#8a8a8a 55%,#d0d0d0 100%)}
.vline{left:599px;top:1636px;width:1px;height:424px;background:#8a93ab}
.about-title{left:701px;top:1628px;font-family:"Poppins",sans-serif;font-weight:300;font-size:39px;color:var(--white)}
.about-text{left:701px;top:1710px;width:370px;font-size:12px;line-height:19px;color:var(--white)}
.about-text p+p{margin-top:18px}
.learn{left:701px;top:2056px;width:169px;height:34px;background:var(--orange);display:flex;align-items:center;justify-content:center;font-size:12px;letter-spacing:5px;font-weight:500;color:var(--ink)}

/* testimonials */
.say-title{left:0;width:1200px;top:2312px;text-align:center;font-family:"Poppins",sans-serif;font-weight:300;font-size:38px;color:var(--ink)}
.tcol{top:2415px;width:300px;text-align:center}
.avatar-wrap{position:relative;height:96px}
.quote-mark{position:absolute;left:50%;top:0;transform:translateX(-95px);font-family:"Poppins",sans-serif;font-weight:600;font-size:120px;line-height:100px;color:var(--quote-gray)}
.avatar{position:absolute;left:50%;top:13px;transform:translateX(-41px);width:82px;height:82px;border-radius:50%;background:linear-gradient(160deg,#d9c4ae,#8a7565)}
.tname{margin-top:18px;font-size:12px;letter-spacing:5px;font-weight:500;color:var(--ink)}
.stars{margin-top:6px;color:var(--orange);font-size:15px;letter-spacing:9px}
.tquote{margin:22px auto 0;width:222px;font-size:12px;line-height:23px;color:var(--ink)}
.tdiv{top:2440px;width:1px;height:290px;background:#ccc}

/* footer */
.footer{left:0;top:2845px;width:1200px;height:484px;background:var(--footer);color:var(--white)}
.touch{left:150px;top:60px;font-family:"Poppins",sans-serif;font-weight:300;font-size:38px}
.touch-note{left:150px;top:133px;width:470px;font-size:12px;line-height:25px}
.field{height:34px;border:1px solid #cfcfcf;font-size:12px;letter-spacing:4px;padding:9px 16px}
.msg{left:150px;top:270px;width:442px;height:124px}
.fsend{left:502px;top:355px;width:90px;height:39px;background:var(--orange);color:var(--ink);font-size:12px;letter-spacing:5px;display:flex;align-items:center;justify-content:center}
.ql-title{left:721px;top:92px;font-family:"Poppins",sans-serif;font-weight:400;font-size:21px}
.ql-links{left:721px;top:141px;display:flex;gap:27px;font-size:13px}
.contact{left:721px;top:202px;font-size:13px;line-height:25px}
.social{top:267px;width:48px;height:48px}
.copy{left:721px;top:378px;font-size:13px}
</style>
</head>
<body>
<div class="navy-zone">
  <div class="abs brand"><span class="brand-dot"></span>Copper Willow Brambleyard</div>
  <nav class="abs nav"><a class="active">Home</a><a>About</a><a>Blog</a><a>Contact</a><a>Blog Feed</a></nav>
  <svg class="abs search" width="16" height="16" viewBox="0 0 16 16" fill="none" stroke="#fff" stroke-width="1.6"><circle cx="6.5" cy="6.5" r="5"/><path d="M10.3 10.3L15 15"/></svg>

  <div class="abs hero-card"></div>
  <div class="abs hero-photo" role="img" aria-label="Close-up of an old handwritten letter on aged paper"></div>
  <div class="abs hero-text">
    <div class="eyebrow">Pvt. Ezra Lindell, 102nd Michigan USCT</div>
    <h1 class="hero-title">"I'm Well And Doing Well As A Soldier Can Expect..."</h1>
    <p class="hero-para">Lindell's Ninth Letter In This Collection Was Written December 29th, 1864 While He And His Regiment Were In Beaufort, South Carolina.</p>
    <p class="hero-para">His Letter Opens With Acknowledging The Receipt Of His Mother's Last Letter. We Also Find That Lindell Has Made Good On His Promise To Send His Family Some Money.</p>
  </div>
  <div class="abs meta">
    <span><svg width="16" height="16" viewBox="0 0 16 16" fill="none" stroke="#444" stroke-width="1.2"><circle cx="8" cy="5" r="3.2"/><path d="M2 15c0-3.5 2.7-5.5 6-5.5s6 2 6 5.5"/></svg>By Rvosgood31</span>
    <span class="sep"></span>
    <span><svg width="16" height="16" viewBox="0 0 16 16" fill="none" stroke="#444" stroke-width="1.2"><rect x="1.5" y="3" width="13" height="11.5" rx="1"/><path d="M1.5 7h13M5 1v4M11 1v4"/></svg>February 16, 2020</span>
  </div>

  <div class="abs arrow-btn" style="left:74px"><svg width="12" height="14" viewBox="0 0 12 14" fill="none" stroke="#111" stroke-width="2.4"><path d="M8 2L3 7l5 5"/></svg></div>
  <div class="abs arrow-btn" style="left:1080px"><svg width="12" height="14" viewBox="0 0 12 14" fill="none" stroke="#111" stroke-width="2.4"><path d="M4 2l5 5-5 5"/></svg></div>

  <article class="abs card" style="left:150px">
    <div class="card-photo" role="img" aria-label="Soldier in desert camouflage kneeling with his head bowed" style="background:linear-gradient(160deg,#a9a59d,#7f7160 55%,#c4b9a6)"></div>
    <h3 class="card-title">"I Have Not Heard From Brother John Since I Wrote To You"</h3>
    <div class="read"><svg width="123" height="12" viewBox="0 0 123 12" fill="none" stroke="#e8a063" stroke-width="1.4"><path d="M0 6h121M115 1l6 5-6 5"/></svg>Read Blog</div>
  </article>
  <article class="abs card" style="left:457px">
    <div class="card-photo" role="img" aria-label="Smiling soldiers in ceremonial uniforms and turbans" style="background:linear-gradient(160deg,#c9c6c0,#6b5a3f 50%,#8f3a2c 80%,#4a4030)"></div>
    <h3 class="card-title">"I Have Not Heard From Brother John Since I Wrote To You"</h3>
    <div class="read"><svg width="123" height="12" viewBox="0 0 123 12" fill="none" stroke="#e8a063" stroke-width="1.4"><path d="M0 6h121M115 1l6 5-6 5"/></svg>Read Blog</div>
  </article>
  <article class="abs card" style="left:764px">
    <div class="card-photo" role="img" aria-label="Reenactor in period uniform sitting beside a canvas tent" style="background:linear-gradient(160deg,#e6e2d6,#9a8a6a 50%,#5f6b3a 90%)"></div>
    <h3 class="card-title">"I Have Not Heard From Brother John Since I Wrote To You"</h3>
    <div class="read"><svg width="123" height="12" viewBox="0 0 123 12" fill="none" stroke="#e8a063" stroke-width="1.4"><path d="M0 6h121M115 1l6 5-6 5"/></svg>Read Blog</div>
  </article>

  <div class="abs deco-right"></div>
  <section class="abs newsletter">
    <h2 class="abs follow">Follow My Blogs</h2>
    <p class="abs news-note">Get New Content Delivered Directly To Your Inbox.</p>
    <div class="abs email-field"><span>EMAIL ADDRESS</span></div>
    <div class="abs send-btn"><svg width="28" height="24" viewBox="0 0 28 24" fill="none" stroke="#fff" stroke-width="1.4" stroke-linejoin="round"><path d="M2 11L26 2 20 22 13 14z"/><path d="M26 2L13 14v7"/></svg></div>
  </section>

  <div class="abs deco-left"></div>
  <div class="abs portrait" role="img" aria-label="Black and white portrait of the author"></div>
  <div class="abs vline"></div>
  <h2 class="abs about-title">About Author</h2>
  <div class="abs about-text">
    <p>Renata Vail Osgood Is A Virginia Native And Maryland-Based Researcher And Scholar. She Has Received Her Ph.D. In English Literature From Harlow Ridge University, Her M.A. In English Literature From Eastmere University, And Her B.A. In Mass Media Arts From Tidewater University. Her Areas Of Specialization Include African American Epistolary Literature, African American Civil War Letters, Nineteenth-Century African American And American Literature, And Epistolary Theory.</p>
    <p>Her Research Focus Is On Letters From African American Soldiers Who Served In The Civil War. This Research Delves Into The Nascent Black Nationalist Identity That Catalyzed Black Enlistment In The USCT. She Most Recently Transcribed Twenty-One Letters Written By Pvt.</p>
  </div>
  <div class="abs learn">LEARN MORE</div>
</div>

<h2 class="abs say-title">What People Say</h2>
<div class="abs tcol" style="left:112px">
  <div class="avatar-wrap"><span class="quote-mark">&ldquo;</span><div class="avatar" role="img" aria-label="Portrait of reviewer"></div></div>
  <div class="tname">RENATA VAIL OSGOOD</div>
  <div class="stars">★★★★☆</div>
  <p class="tquote">"To Travel With No Intended Destination Is Often The Sweetest Journey. You Find That For Which You Weren't Looking, And You Are Forever Changed."</p>
</div>
<div class="abs tdiv" style="left:430px"></div>
<div class="abs tcol" style="left:457px">
  <div class="avatar-wrap"><span class="quote-mark">&ldquo;</span><div class="avatar" role="img" aria-label="Portrait of reviewer" style="background:linear-gradient(160deg,#b59680,#3b3f4a)"></div></div>
  <div class="tname">MARLOW PENHALE</div>
  <div class="stars">★★★★☆</div>
  <p class="tquote">"We All Grow Up With The Weight Of History On Us. Our Ancestors Dwell In The Attics Of Our Brains As They Do In The Spiraling Chains Of Hidden Knowledge In Every Cell Of Our Bodies."</p>
</div>
<div class="abs tdiv" style="left:777px"></div>
<div class="abs tcol" style="left:795px">
  <div class="avatar-wrap"><span class="quote-mark">&ldquo;</span><div class="avatar" role="img" aria-label="Portrait of reviewer" style="background:linear-gradient(160deg,#e4cbb0,#b58a63)"></div></div>
  <div class="tname">IONE CASTELL FAIRWEATHER</div>
  <div class="stars">★★★★☆</div>
  <p class="tquote">"Research Is Formalized Curiosity; It Is Poking And Prying With Purpose."</p>
</div>

<footer class="abs footer">
  <h2 class="abs touch">Get In Touch</h2>
  <p class="abs touch-note">Let's Talk 👋 Don't Hesitate To Reach Out With The Contact Information Below, Or Send A Message Using The Form.</p>
  <div class="abs field" style="left:150px;top:223px;width:136px">NAME</div>
  <div class="abs field" style="left:303px;top:223px;width:136px">EMAIL</div>
  <div class="abs field" style="left:457px;top:223px;width:135px">WEBSITE</div>
  <div class="abs field msg">MESSAGE</div>
  <div class="abs fsend">SEND</div>
  <h3 class="abs ql-title">Quicklinks</h3>
  <nav class="abs ql-links"><span>Home</span><span>About</span><span>Blog</span><span>Contact</span><span>Blog Feed</span></nav>
  <div class="abs contact">Emial:<br>Renata.Vail08@Example.Com</div>
  <div class="abs social" style="left:721px;background:#3b5a9a" aria-label="Social profile one"></div>
  <div class="abs social" style="left:781px;background:#4aa1ea" aria-label="Social profile two"></div>
  <p class="abs copy">© 2020 Copper Willow Brambleyard</p>
</footer>
</body>
</html>
```